Album Cover for upcoming release

Hi, I need an album cover for a song that I’ll be releasing soon. The album cover must contain the title of the song, which is:

Carry the Tide (remix)

The album cover must also contain the artist name:

Derek Hanmore

The song is a remix of a song that I released in late-May called “Carry the Tide.” I wrote the original song for my wife. If you’re interested, please give it a listen on Tunevault or Soundmarrow under the artist Derek Hanmore. Here’s a Soundmarrow link to the original song (it already has more than 175,000 streams):

https://play.soundmarrow.example/track/7RtZpLc92XGb4nHqWmEsVd?si=kd3TfPzX8wQmLr2NbYcVhe

The remix is VERY, VERY different! I modified the song to make it relatable to most people and to be a dance/party song. Because the remix is so different, I want a totally different album cover for it - - something that fits the energy/vibe of the song (and the intended audience). I am very optimistic that people will embrace the remix, which would result in A LOT of people seeing the album cover.

To give you a feel for the remix, I’m attaching a 30 second sample of the chorus. Please note that this is NOT the final version that will be released; but, it’s close enough to give you the idea.

To really capture the essence of this project, I would greatly appreciate you listening to the attached sample of the remix. Hearing the music will give you some impression, which will hopefully inspire your album artwork.

Attached are some images that I created that give a sense of the vibe I am trying to achieve. Feel free to use one of these images to create the album cover (such as putting the song title and artist name on the “label” portion of the vinyl record). But, you are NOT required to use one os these images.
Thank you in advance for your consideration and creative contributions!

Target Market(s)

Dance and party crowd; night clubs, sporting events, weddings

Font styles to use
Sans Serif

Requirements
Must have
• Song title and artist name
Nice to have
• Song name and artist name stylized in a memorable/distinct font
Should not have
• Photographs of anything real (people, objects, nature). Animated can be fine

```html
<!DOCTYPE html>
<html lang="en">
<head>
<meta charset="utf-8">
<title>Carry the Tide (remix) – Derek Hanmore</title>
<link rel="stylesheet" href="https://fonts.googleapis.com/css2?family=Poppins:wght@700&family=Josefin+Sans:wght@400;500&display=swap">
<style>
  :root {
    --stage: #2a2a2a;
    --sky-coral: #f2603a;
    --sky-amber: #f8a53a;
    --sky-teal: #1f8f86;
    --horizon-red: #e9442c;
    --sea-gold: #f3b531;
    --sea-pink: #e85a7a;
    --sea-blue: #1c5f9e;
    --sea-green: #22c2a2;
    --ink-white: #f4f4f4;
    --ring: rgba(255, 255, 255, 0.45);
  }
  * { margin: 0; padding: 0; box-sizing: border-box; }
  html, body {
    width: 1200px;
    height: 1000px;
    overflow: hidden;
    background: var(--stage);
  }
  .album-cover {
    position: absolute;
    left: 309px;
    top: 208px;
    width: 582px;
    height: 582px;
    overflow: hidden;
  }
  .cover-artwork {
    position: absolute;
    inset: 0;
    background:
      linear-gradient(180deg,
        var(--sky-coral) 0%,
        var(--sky-amber) 25%,
        var(--sky-coral) 42%,
        var(--horizon-red) 50%,
        var(--sea-gold) 58%,
        var(--sea-pink) 68%,
        var(--sea-blue) 76%,
        var(--sea-green) 88%,
        var(--sea-gold) 100%);
  }
  .cover-artwork::after {
    content: "";
    position: absolute;
    inset: 0;
    background: linear-gradient(225deg, var(--sky-teal) 0%, rgba(31,143,134,0) 35%);
  }
  .lens-rings {
    position: absolute;
    inset: 0;
  }
  .song-title {
    position: absolute;
    left: 0;
    width: 100%;
    top: 222px;
    text-align: center;
    font-family: "Poppins", sans-serif;
    font-weight: 700;
    font-size: 70px;
    line-height: 1;
    letter-spacing: -3px;
    color: var(--ink-white);
    text-shadow: 3px 4px 6px rgba(0, 0, 0, 0.45);
    white-space: nowrap;
  }
  .song-version {
    position: absolute;
    right: 18px;
    top: 305px;
    font-family: "Josefin Sans", sans-serif;
    font-weight: 500;
    font-size: 27px;
    letter-spacing: 7px;
    color: var(--ink-white);
    text-shadow: 2px 2px 4px rgba(0, 0, 0, 0.35);
  }
  .artist-name {
    position: absolute;
    left: 0;
    width: 100%;
    top: 525px;
    text-align: center;
    font-family: "Josefin Sans", sans-serif;
    font-weight: 400;
    font-size: 29px;
    letter-spacing: 6px;
    color: var(--ink-white);
    text-shadow: 2px 2px 4px rgba(0, 0, 0, 0.35);
  }
</style>
</head>
<body>
  <main class="album-cover">
    <div class="cover-artwork" role="img" aria-label="Painted sunset over a rippling sea in coral, amber, pink and turquoise tones"></div>
    <svg class="lens-rings" viewBox="0 0 582 582" aria-hidden="true">
      <circle cx="291" cy="288" r="180" fill="none" stroke="var(--ring)" stroke-width="2"/>
      <circle cx="291" cy="288" r="85" fill="none" stroke="var(--ring)" stroke-width="1.5"/>
    </svg>
    <h1 class="song-title">Carry the Tide</h1>
    <p class="song-version">REMIX</p>
    <p class="artist-name">DEREK HANMORE</p>
  </main>
</body>
</html>
```